Business cards for a tribute and obituary website

Our website is called Quiet Orchard.

It is a special place online for people to remember their loved ones who have passed away, through obituaries and tributes. Friends and family can also convey their condolences on the deceased's memorial page. Celebrating the life of the deceased and remembering their legacy is very important to us – death should not be just about grieving.

We would like the card to look tasteful and modern. The design should ideally not have colours that are too bright. The logo and website URL, www.quietorchardpages.net should be visible on the front of the card, with our slogan "Celebrating a life passed" on the back.

The design should communicate our purpose – remembering loved ones who have passed – and also a lighter tone of celebrating life. It should not look like a funeral director's card!

Our logo has been attached. Looking forward to some beautiful designs! Get creative :)
Updates

Reason: Thank you all for your designs. The rest of my team and I have not reached a decision on which design to select and I am collecting feedback from them. I will provide feedback for any changes that need to be made soon. It would be great if we could see more original designs and in more colours! We will definitely select a design by this deadline.

Industry/Entity Type

Business

Contact Information for Business Card

Nadia Fenwick
Project Manager
471226809
nadiafenwick@quietorchardpages.net

Font styles to use
Serif
Sans Serif

Requirements
Must have
• Logo and website address (www.quietorchardpages.net) on the front.
Nice to have
• Hi designers! It would be nice to see alternative colours – feel free to try out colours that are tasteful and subtle. The colour of the business card does not have to be the same as the logo.
• We would also like to see the logo used in different ways, perhaps a glossy or embossed finish. The card should look stylish.

```html
<!DOCTYPE html>
<html lang="en">
<head>
<meta charset="utf-8">
<title>Quiet Orchard — Business Card</title>
<link href="https://fonts.googleapis.com/css2?family=Bitter:wght@700&family=Crimson+Text:wght@400;600&display=swap" rel="stylesheet">
<style>
  :root {
    --backdrop: #cde9e0;
    --teal-light: #3ea3a8;
    --teal-mid: #1b8a8c;
    --teal-deep: #006e71;
    --teal-ink: #0d6664;
    --paper: #ffffff;
    --white-text: #f4fbfa;
    --slogan-ink: #4c6c64;
    --band: #e3efeb;
    --emboss: #e9eeed;
    --rule: rgba(10, 90, 88, 0.55);
  }
  * { box-sizing: border-box; margin: 0; padding: 0; }
  html, body {
    width: 1200px;
    height: 856px;
    overflow: hidden;
    background: var(--backdrop);
  }
  .sheet {
    width: 1200px;
    height: 856px;
    display: flex;
    align-items: center;
    justify-content: center;
    gap: 64px;
  }
  .card {
    position: relative;
    width: 504px;
    height: 288px;
    border-radius: 28px;
    overflow: hidden;
    box-shadow: 0 6px 18px rgba(40, 90, 80, 0.18);
  }

  /* Front */
  .card-front {
    background: linear-gradient(160deg, var(--teal-light) 0%, var(--teal-mid) 55%, var(--teal-deep) 100%);
    padding: 30px 36px;
    font-family: "Crimson Text", Georgia, serif;
    color: var(--white-text);
  }
  .brand {
    display: flex;
    align-items: center;
    gap: 14px;
  }
  .brand-dot {
    width: 38px;
    height: 38px;
    border-radius: 50%;
    background: var(--teal-ink);
  }
  .brand-name {
    font-family: "Bitter", Georgia, serif;
    font-weight: 700;
    font-size: 31px;
    color: var(--teal-ink);
    letter-spacing: 0.5px;
  }
  .brand-rule {
    margin: 16px 0 8px;
    width: 220px;
    height: 1px;
    background: var(--rule);
  }
  .site-url {
    font-size: 15px;
    color: var(--teal-ink);
    letter-spacing: 0.3px;
  }
  .person {
    margin-top: 26px;
  }
  .person-name {
    font-size: 20px;
    font-variant: small-caps;
    letter-spacing: 1px;
    line-height: 1;
  }
  .person-role {
    font-size: 10px;
    font-weight: 600;
    text-transform: uppercase;
    letter-spacing: 0.8px;
    margin-top: 3px;
  }
  .contact {
    position: absolute;
    left: 36px;
    bottom: 24px;
    font-size: 16px;
    line-height: 1.35;
  }

  /* Back */
  .card-back {
    background: var(--paper);
  }
  .back-band {
    position: absolute;
    left: -60px;
    top: 108px;
    width: 640px;
    height: 76px;
    background: var(--band);
    transform: rotate(-14deg);
  }
  .back-name {
    position: absolute;
    top: 26px;
    right: 34px;
    font-family: "Bitter", Georgia, serif;
    font-weight: 700;
    font-size: 22px;
    color: var(--emboss);
  }
  .slogan {
    position: absolute;
    left: 0;
    right: 0;
    top: 104px;
    text-align: center;
    font-family: "Crimson Text", Georgia, serif;
    font-size: 32px;
    line-height: 1.05;
    text-transform: uppercase;
    letter-spacing: 1.5px;
    color: var(--slogan-ink);
  }
</style>
</head>
<body>
  <main class="sheet">
    <section class="card card-front" aria-label="Card front">
      <div class="brand">
        <span class="brand-dot" aria-hidden="true"></span>
        <span class="brand-name">Quiet Orchard</span>
      </div>
      <div class="brand-rule"></div>
      <p class="site-url">www.quietorchardpages.net</p>
      <div class="person">
        <p class="person-name">Nadia Fenwick</p>
        <p class="person-role">Project Manager</p>
      </div>
      <div class="contact">
        <p class="contact-phone">471.226 809</p>
        <p class="contact-email">nadiafenwick@quietorchardpages.net</p>
      </div>
    </section>

    <section class="card card-back" aria-label="Card back">
      <div class="back-band" aria-hidden="true"></div>
      <p class="back-name">Quiet Orchard</p>
      <h2 class="slogan">Celebrating<br>a life passed</h2>
    </section>
  </main>
</body>
</html>
```